Business Card design for new private practice opening

I need a business card design for my new private practice with my new logo uploaded as a file
On the front the logo
On the back: maybe a small logo somewhere?
Priv. Doz. DDr. Corinna Vestaluk
Fachärztin für Allgemein- & Viszeralchirurgie
Address: xxx
Tel: xxx
Mobil:xxx
Webseite:xxx
Email:xxx

Contact Information for Business Card

See project description above for details

Requirements
Nice to have
• I would like the colors of the logo incorporated into the business card

```html
<!DOCTYPE html>
<html lang="de">
<head>
<meta charset="utf-8">
<title>Vestaluk Chirurgie – Visitenkarte</title>
<link href="https://fonts.googleapis.com/css2?family=Montserrat:wght@600;700&family=Nunito:wght@400;600&display=swap" rel="stylesheet">
<style>
  :root {
    --teal: #5bb6b1;
    --teal-soft: #cfe7e5;
    --teal-mist: #e6f2f1;
    --grey: #808285;
    --grey-dark: #6d6f72;
    --card: #ffffff;
    --backdrop: #eeeff0;
  }
  * { margin: 0; padding: 0; box-sizing: border-box; }
  html, body { width: 1200px; height: 800px; overflow: hidden; }
  body {
    background: var(--backdrop);
    position: relative;
    font-family: "Nunito", sans-serif;
    color: var(--grey);
  }
  .card {
    position: absolute;
    width: 600px;
    height: 343px;
    background: var(--card);
    box-shadow: 0 6px 18px rgba(0,0,0,0.10);
    overflow: hidden;
  }
  .card-front { left: 60px; top: 40px; }
  .card-back { left: 540px; top: 417px; }

  .card-waves { position: absolute; left: 0; bottom: 0; width: 100%; height: 140px; }

  /* front */
  .brand {
    position: absolute;
    left: 95px; top: 105px;
    display: flex; align-items: center; gap: 26px;
  }
  .brand-circle {
    width: 120px; height: 120px;
    border: 5px solid var(--grey);
    border-radius: 50%;
  }
  .brand-name {
    font-family: "Montserrat", sans-serif;
    font-weight: 700;
    font-size: 44px;
    line-height: 1.1;
    letter-spacing: 1px;
    color: var(--grey);
    text-transform: uppercase;
  }

  /* back */
  .header {
    position: absolute;
    left: 30px; top: 28px;
    display: flex; align-items: center; gap: 20px;
  }
  .header-circle {
    width: 82px; height: 82px;
    border: 4px solid var(--grey);
    border-radius: 50%;
  }
  .person-name {
    font-family: "Montserrat", sans-serif;
    font-weight: 700;
    font-size: 21px;
    color: var(--grey);
  }
  .person-title {
    font-size: 17px;
    color: var(--grey);
    margin-top: 4px;
    padding-bottom: 4px;
  }
  .header-rule {
    position: absolute;
    left: 0; top: 124px; width: 100%; height: 20px;
  }
  .contacts {
    position: absolute;
    top: 160px; left: 50px; right: 40px;
    display: grid;
    grid-template-columns: 290px 1fr;
  }
  .contact-col { display: flex; flex-direction: column; gap: 20px; }
  .contact-col + .contact-col {
    border-left: 1px solid #c8c9cb;
    padding-left: 32px;
    margin-top: -14px;
  }
  .contact-item { display: flex; align-items: center; gap: 12px; font-size: 17px; }
  .contact-icon { width: 20px; height: 20px; fill: var(--grey); flex: none; }
</style>
</head>
<body>

<section class="card card-front" aria-label="Vorderseite">
  <div class="brand">
    <div class="brand-circle"></div>
    <div class="brand-name">Vestaluk<br>Chirurgie</div>
  </div>
  <svg class="card-waves" viewBox="0 0 600 140" preserveAspectRatio="none" aria-hidden="true">
    <path d="M0 105 Q320 110 600 20 L600 140 L0 140 Z" fill="var(--teal-mist)"/>
    <path d="M0 115 Q330 125 600 40 L600 48 Q330 132 0 126 Z" fill="var(--teal)"/>
    <path d="M0 130 Q330 138 600 60 L600 140 L0 140 Z" fill="#fff"/>
  </svg>
</section>

<section class="card card-back" aria-label="Rückseite">
  <header class="header">
    <div class="header-circle"></div>
    <div>
      <div class="person-name">Priv. Doz. DDr. Corinna Vestaluk</div>
      <div class="person-title">Fachärztin für Allgemein- &amp; Viszeralchirurgie</div>
    </div>
  </header>
  <svg class="header-rule" viewBox="0 0 600 20" preserveAspectRatio="none" aria-hidden="true">
    <path d="M0 14 L600 2 L600 3 L0 18 Z" fill="var(--teal)"/>
  </svg>

  <div class="contacts">
    <div class="contact-col">
      <div class="contact-item">
        <svg class="contact-icon" viewBox="0 0 24 24"><path d="M12 2a7 7 0 0 0-7 7c0 5 7 13 7 13s7-8 7-13a7 7 0 0 0-7-7zm0 9.5A2.5 2.5 0 1 1 12 6.5a2.5 2.5 0 0 1 0 5z"/></svg>
        <span>Address: xxx</span>
      </div>
      <div class="contact-item">
        <svg class="contact-icon" viewBox="0 0 24 24"><path d="M6.6 10.8a15 15 0 0 0 6.6 6.6l2.2-2.2a1 1 0 0 1 1-.25 11.4 11.4 0 0 0 3.6.57 1 1 0 0 1 1 1V20a1 1 0 0 1-1 1A17 17 0 0 1 3 4a1 1 0 0 1 1-1h3.5a1 1 0 0 1 1 1c0 1.25.2 2.45.57 3.57a1 1 0 0 1-.25 1z"/></svg>
        <span>Tel: xxx</span>
      </div>
      <div class="contact-item">
        <svg class="contact-icon" viewBox="0 0 24 24" fill="none" stroke="var(--grey)" stroke-width="1.6"><circle cx="12" cy="12" r="9"/><ellipse cx="12" cy="12" rx="4" ry="9"/><path d="M3 12h18M5 7h14M5 17h14"/></svg>
        <span>Webseite: xxx</span>
      </div>
    </div>
    <div class="contact-col">
      <div class="contact-item">
        <svg class="contact-icon" viewBox="0 0 24 24" fill="none" stroke="var(--grey)" stroke-width="2"><rect x="6" y="2" width="12" height="20" rx="2"/><path d="M10 18h4"/></svg>
        <span>Tel: xxx</span>
      </div>
      <div class="contact-item">
        <svg class="contact-icon" viewBox="0 0 24 24" fill="none" stroke="var(--grey)" stroke-width="2"><rect x="6" y="2" width="12" height="20" rx="2"/><path d="M10 18h4"/></svg>
        <span>Mobil:xxx</span>
      </div>
      <div class="contact-item">
        <svg class="contact-icon" viewBox="0 0 24 24"><path d="M2 5h20v14H2z"/><path d="M2 5l10 8 10-8" fill="none" stroke="#fff" stroke-width="1.6"/></svg>
        <span>Email: xxx</span>
      </div>
    </div>
  </div>

  <svg class="card-waves" viewBox="0 0 600 140" preserveAspectRatio="none" aria-hidden="true">
    <path d="M0 95 Q330 120 600 60 L600 140 L0 140 Z" fill="var(--teal-mist)"/>
    <path d="M0 105 Q330 128 600 72 L600 76 Q330 133 0 110 Z" fill="var(--teal-soft)"/>
    <path d="M0 118 Q330 135 600 88 L600 140 L0 140 Z" fill="var(--teal-soft)" opacity="0.7"/>
  </svg>
</section>

</body>
</html>
```